taLUMa - 3 Etiketten für naturbelassenes Speiseöl - Leinöl, Leindotteröl und Rapsöl
Zielgruppe
Wir sind ein junges Startup mit der Ziel, die besten, gesündesten Omega3-Öle in bester handwerklicher Qualität anzubieten. Vor allem soll das folgende Unterscheidungsmerkmal unsere Marke verkörpern: in Supermärkten und Discountern gibt es überwiegend denaturierte Öle, das heißt extrahierte und raffinierte Öle. Dadurch sind diese zwar länger haltbar, jedoch wertlos für den Körper. Wir wollen Öle voller Naturkraft anbieten und lassen daher die bei Ölpressung entstehenden Schwebestoffe im Form gesunder sekundärer Pflanzenstoffe bewusst im Öl und filtern diese nicht heraus.
Unser Markenname - taLUMa … mit dem Slogan ' taLUMa sein heißt für uns: dynamisch, kraftvoll, vital, frohen Mutes und voller Lebendigkeit - genauso ist unser Öl. Frisch gepresst in bester handwerklicher Qualität, naturbelassen voller gesunder sekundärer Pflanzenstoffe und reich an lebenswichtigen Omega3-Fettsäuren.'
Fokus der taLUMa-Ölmanufakur: echtes Handwerk, beste Qualität, pure Leidenschaft, wahre Nachhaltigkeit und authentische Regionalität!
Aufgabenstellung
In Summe benötigen wir 3 Etiketten für 3 verschiedene Speiseöle: Leinöl, Leindotteröl und Rapsöl.
Für diese drei Öle benötigen wir das Design kreativer, ansprechender Etiketten mit folgenden Prämissen:
A. Etiketten im Tafelkreidestil (Chalk-Handlettering): gemäß unser Vision wollen wir die besten, gesündesten Omega3-Öle in bester handwerklicher Qualität anbieten - diesen Aspekt soll das Look&Feel der Ölflasche samt Etikett verkörpern. Abgefüllt wird unser Öl in hochwertige mattschwarze Steinzeugölflaschen mit Holzkorkverschluss (siehe beigefügtes Bild). Durch das matte schwarz der Ölfalsche soll grundsätzlich das Etiketten-Design im Tafelkreidestil (Chalk-Handlettering) mit einem kreativen Mix aus schönen (gut lesbaren) Schriften und graphischen Elementen sein. Das Endprodukt des Etiketts soll ein transparenter Aufkleber sein, der auf die Flasche geklebt wird.
Maximale Größe des Etiketts: 200ml Flasche max. 13,5 cm Höhe x max. 17 cm Breite
Hinweis: das Etikett soll für die Größe der 200ml Flasche konzipiert werden, jedoch idealerweise so skalierbar sein, daß es auch auf die Größe einer 500 ml-Flasche angepasst werden kann; Größe der 500 ml Flasche max. Höhe 17 cm x max. Breite 21,5 cm
B. Pflanzen-/Saatenzweig als graphisches Unterscheidungsmerkmal des Öls: idealerweise wird das jeweilige Öl (Rapsöl, Leinöl und Leindotteröl) mit einem graphischen Pflanzenzweig der jeweiligen Ölsaat gekennzeichnet.
C. Was macht dies Öl so wertvoll? - die wichtigen und wertvollsten Inhaltsstoffe des jeweiligen Öls sollen herausgestellt werden.
Bein Leinöl und Leindotteröl ist dies vor allem der hohe Gehalt an Omega3-Fettsäuren - dies macht das Öl so besonders wertvoll
Graphisches Textelement mit 'Der Omega3 Booster fur den Körper' (oder der “Powerlieferant” für Omega 3)
Gut für: Herz-Kreislaufszsystem stärken
Gehirnleistung steigern
Blu..

```html
<!DOCTYPE html>
<html lang="de">
<head>
<meta charset="utf-8">
<title>taLUMa – Etiketten Speiseöl</title>
<link rel="stylesheet" href="https://fonts.googleapis.com/css2?family=Special+Elite&family=Oswald:wght@300;400&display=swap">
<style>
  :root {
    --canvas: #ffffff;
    --bottle-black: #1b1a1e;
    --chalk: #f2f2ef;
    --chalk-soft: #b9b9b9;
    --omega-green: #5a7d2a;
    --flax-blue: rgba(63, 79, 208, 0.85);
    --camelina-green: rgba(143, 157, 78, 0.8);
    --rape-yellow: rgba(201, 189, 74, 0.8);
    --sketch-tint: rgba(255, 255, 255, 0.05);
  }
  * { box-sizing: border-box; margin: 0; padding: 0; }
  html, body { width: 1200px; height: 1077px; overflow: hidden; background: var(--canvas); }
  .label-row { position: relative; width: 1200px; height: 1077px; }
  .label {
    position: absolute; top: 190px; width: 290px; height: 810px;
    background: var(--bottle-black); border-radius: 28px;
  }
  .label--lein { left: 105px; }
  .label--leindotter { left: 460px; }
  .label--raps { left: 805px; }

  .brand {
    position: absolute; top: 96px; left: 0; width: 100%;
    display: flex; justify-content: center; align-items: center; gap: 8px;
    font-family: "Oswald", sans-serif; font-weight: 300; font-size: 24px;
    color: var(--chalk); letter-spacing: 1px;
  }
  .brand-dot { width: 12px; height: 12px; border-radius: 50%; background: var(--chalk); }

  /* Pflanzenzweig-Fläche mit Aquarellkreis, liegt hinter der Schrift */
  .plant {
    position: absolute; z-index: 0; width: 90px; border-radius: 45px;
  }
  .label--lein .plant {
    left: 60px; top: 340px; height: 380px;
    background:
      radial-gradient(circle at 40% 110px, var(--flax-blue) 0 34px, transparent 35px),
      linear-gradient(var(--sketch-tint), var(--sketch-tint));
  }
  .label--leindotter .plant {
    left: 50px; top: 330px; height: 380px;
    background:
      radial-gradient(circle at 52% 116px, var(--camelina-green) 0 40px, transparent 41px),
      linear-gradient(var(--sketch-tint), var(--sketch-tint));
  }
  .label--raps .plant {
    left: 55px; top: 340px; height: 380px;
    background:
      radial-gradient(circle at 50% 106px, var(--rape-yellow) 0 36px, transparent 37px),
      linear-gradient(var(--sketch-tint), var(--sketch-tint));
  }

  .oil-name {
    position: absolute; z-index: 1;
    writing-mode: vertical-rl; transform: rotate(180deg);
    font-family: "Special Elite", monospace; font-size: 44px; line-height: 1;
    color: var(--chalk); letter-spacing: 2px;
  }
  .label--lein .oil-name { top: 272px; left: 124px; letter-spacing: 3px; }
  .label--leindotter .oil-name { top: 270px; left: 112px; letter-spacing: 1px; }
  .label--raps .oil-name { top: 280px; left: 124px; letter-spacing: 3px; }

  .omega-badge {
    position: absolute; z-index: 1; top: 298px; left: 172px; width: 54px; height: 54px;
    border-radius: 50%; background: var(--omega-green); opacity: 0.9;
  }

  .qualities {
    position: absolute; z-index: 1; left: 135px; top: 486px; list-style: none;
    font-family: "Oswald", sans-serif; font-weight: 300; font-size: 14.5px;
    line-height: 19px; color: var(--chalk-soft);
  }
  .qualities li { margin-bottom: 11px; }
  .label--leindotter .qualities { left: 176px; top: 470px; }
  .label--raps .qualities { top: 492px; }

  .volume {
    position: absolute; z-index: 1; left: 135px; top: 745px;
    font-family: "Oswald", sans-serif; font-weight: 400; font-size: 26px;
    color: var(--chalk-soft);
  }
  .label--leindotter .volume { left: 176px; top: 732px; }
  .label--raps .volume { top: 748px; }
</style>
</head>
<body>
<main class="label-row">

  <section class="label label--lein">
    <div class="brand"><span class="brand-dot"></span>taLUMa</div>
    <div class="plant" role="img" aria-label="Gezeichneter Leinzweig mit blauer Blüte vor blauem Aquarellkreis"></div>
    <h2 class="oil-name">LEINÖL</h2>
    <div class="omega-badge" aria-hidden="true"></div>
    <ul class="qualities">
      <li>dynamisch</li>
      <li>vital</li>
      <li>kraftvoll</li>
      <li>frisch<br>gepresst</li>
      <li>naturbelassen</li>
      <li>reich an<br>Omega3<br>Fettsäuren</li>
    </ul>
    <p class="volume">200ml</p>
  </section>

  <section class="label label--leindotter">
    <div class="brand"><span class="brand-dot"></span>taLUMa</div>
    <div class="plant" role="img" aria-label="Gezeichneter Leindotterzweig mit Blüten vor grünem Aquarellkreis"></div>
    <h2 class="oil-name">LEINDOTTERÖL</h2>
    <div class="omega-badge" aria-hidden="true"></div>
    <ul class="qualities">
      <li>dynamisch</li>
      <li>vital</li>
      <li>kraftvoll</li>
      <li>frisch<br>gepresst</li>
      <li>naturbelassen</li>
      <li>reich an<br>Omega3<br>Fettsäuren</li>
    </ul>
    <p class="volume">200ml</p>
  </section>

  <section class="label label--raps">
    <div class="brand"><span class="brand-dot"></span>taLUMa</div>
    <div class="plant" role="img" aria-label="Gezeichneter Rapszweig mit Blüten vor gelbem Aquarellkreis"></div>
    <h2 class="oil-name">RAPSÖL</h2>
    <div class="omega-badge" aria-hidden="true"></div>
    <ul class="qualities">
      <li>dynamisch</li>
      <li>vital</li>
      <li>kraftvoll</li>
      <li>frisch<br>gepresst</li>
      <li>naturbelassen</li>
      <li>reich an<br>Omega3<br>Fettsäuren</li>
    </ul>
    <p class="volume">200ml</p>
  </section>

</main>
</body>
</html>
```